Website design for Australia Equine Insurance business

Website Design Brief
1. Introduction
This brief guides the development of a modern, interactive website for our next-generation equine insurance business. We aim to establish a strong digital presence with a website that embodies innovation, usability, and trust, leading to exceptional user experiences and high customer conversions.

2. Company Background
Our startup offers cutting-edge equine insurance solutions across Australia, leveraging emerging technologies for smarter risk assessment, customer engagement, and claims processing. Our commitment is to protect our customers' financial interests and their equine companions with unparalleled service and modern, flexible insurance options.

3. Objectives
The website should:

Highlight our innovative products, services, and unique value proposition.
Drive lead generation and customer conversion using engaging design elements and compelling CTAs.
Foster customer trust and loyalty through transparency, industry expertise, and interactive features.
Enable users to request quotes, purchase insurance, and file claims online in a seamless, intuitive manner.
Be responsive and user-friendly across all devices.

5. Design Requirements
Look and Feel
The design should reflect our brand's personality: innovative, modern, reliable, and committed to the equine community. It should use our brand colours and logo, ensuring a clean, fresh aesthetic. The style guide should promote consistency across fonts, buttons, form fields, etc.

User Interface
The website should display optimally across desktop, tablet, and mobile, with a focus on usability and accessibility. Clear navigation menus, intuitive search and filters, and easy access to important pages like "Get a Quote," "File a Claim," "Contact Us," etc., should be ensured.

Content
Content should be engaging, easily digestible, and serve to educate users about our unique services and the value of equine insurance. The site should also feature blog posts, video guides, and interactive FAQs to illustrate our industry expertise and the benefits of our next-gen approach.

Functionality
Smart Quote Calculator: An AI-driven quote calculator providing real-time estimates.
Digital Purchase and Claims: Facilitate insurance purchase and claims filing digitally, complemented by AI and blockchain tech for efficiency and transparency.
User Accounts: Customers should be able to manage their policies, payments, and claims through personalized accounts.
AI Chatbot: Implement a chatbot for automated customer support, query resolution, and guidance.
SEO and Analytics: Ensure the website is SEO-optimized and integrated with analytics tools like Google Analytics.
6. Timeline
We aim to complete the website design and development project within a 4-month timeframe, given the startup nature of our business. This includes stages of initial design, content creation, development, testing, and launch.

7. Budget
We understand the importance of investing in quality and are open to reasonable negotiations for ensuring the best output.

Target Market(s)

4. Target Audience Our target audience is tech-savvy horse owners, breeders, trainers, equestrian centres, and younger individuals interested in equine ownership, primarily aged between 18-45. They appreciate digital convenience, technological innovation, and quality service.

Industry/Entity Type

The equine insurance industry is a specialised branch of the broader insurance market, focusing on coverage for all things related to horses. It encompasses a wide range of coverage areas such as mortality insurance (life insurance for horses), medical coverage, loss of use, liability coverage, and more. The industry is one of passion and care, where the clientele often form a deeply emotional connection to their insured assets - their horses. It’s characterized by a strong focus on well-being, safety, and the financial protection of both the horses and their owners. This makes trust, professionalism, and expertise central to any successful equine insurance business. Our new venture is positioned as a next-generation equine insurance provider. This means we are blending traditional insurance offerings with cutting-edge technologies such as AI and machine learning for better risk assessment, seamless customer service, and efficient claims processing. The audience in this sector is diverse, ranging from individual horse owners and breeders to professional trainers and large equestrian centres. Many of our customers have a significant emotional and financial investment in their horses, so they need to feel reassured that their insurance provider understands and respects this. In designing for this industry, it's essential to strike a balance between sophistication and warmth, to reflect both our professional reliability and our understanding of the personal passion that drives our clients. The design needs to feel modern and innovative, signaling our next-gen approach, but also trustworthy and user-friendly, ensuring customers of all technological skill levels feel comfortable using our platform. Moreover, the design should convey a sense of our commitment to the equine community, showing that we're more than just a faceless corporation. We care deeply about the wellbeing of horses and their owners, and we're here to support them with quality insurance solutions tailored to their unique needs.

Coding

Coded - Design and coding required

Number of Pages Required

5+ page

Requirements
Must have
• Responsive Design: The website should be fully responsive, offering optimal viewing and interaction across a range of devices - desktop, tablet, and mobile. Intuitive Navigation: The site should feature an easy-to-understand navigation system that allows users to find the information they're seeking quickly and efficiently. Clear Branding: The design should consistently incorporate the company's logo, colors, and overall aesthetic, reinforcing brand recognition. Content: High-quality, relevant content that explains your services, highlights your unique selling propositions, and educates users about equine insurance. The language should be clear, concise, and engaging. Smart Quote Calculator: An interactive tool enabling potential customers to get real-time insurance quotes. Online Purchase and Claims Filing System: A streamlined, user-friendly process for customers to buy insurance and file claims online. Customer Accounts: A secure area for customers to manage their policies, track claims, and make payments. AI Chatbot: An automated chat feature providing immediate customer support and answering frequently asked questions. SEO Optimization: The site must be search engine friendly, with strategically placed keywords, meta tags, and an XML sitemap for better indexing by search engines. Analytics Integration: Integration with tools like Google Analytics for tracking and analyzing user behavior and site performance. Data Security: Implementation of strong security measures to protect user data, including SSL encryption. Accessibility: Compliance with Web Content Accessibility Guidelines (WCAG) to ensure the site is accessible to people with disabilities. Contact Information: Clearly visible and easily accessible contact details, including phone number, email, and physical address. Social Media Integration: Links to the company's social media profiles for enhanced customer engagement and brand visibility. Remember, while these are essential features, the goal should always be to provide a seamless, positive user experience that aligns with your brand's identity and goals.
Nice to have
• Interactive Features: Interactive elements like quizzes or calculators can engage users, offer value, and make your site more memorable. Video Content: Videos explaining your products, services, or the importance of equine insurance can be a dynamic way to share information and appeal to different learning styles. Live Chat: In addition to an AI chatbot, having a live chat option for immediate customer support could significantly enhance user experience and satisfaction. Personalisation: If your resources allow, personalised content based on user behaviour or preferences can make your website more engaging and relevant. Integrated Blog: A blog section featuring articles on equine health, insurance tips, case studies etc., could help establish your brand as a thought leader in the field and improve SEO. Multilingual Support: If your target audience includes non-English speakers, offering content in multiple languages could be a beneficial feature. Customer Testimonials/Reviews: Including testimonials or reviews from satisfied customers can build trust and offer social proof. Resource Library: A library of downloadable resources (guides, checklists, eBooks) could offer added value to your customers and potential leads. Interactive FAQ: A dynamic FAQ section, where users can find answers quickly, or even an FAQ chatbot, could enhance the user experience. Newsletter Signup: An easily accessible sign-up option for a regular newsletter to keep users informed about your services, industry news, and tips. Integration with Customer Relationship Management (CRM) Software: To manage leads and customer information effectively, if your business operations allow for this level of integration.
Should not have
• Cluttered Layout: Overcrowding pages with too much information, images, or other elements can make your website look messy and confusing, hindering usability. Irrelevant Content: Your website should focus on information that is relevant to your target audience and industry. Avoid including content that does not provide value or enhance understanding of your products or services. Complex Navigation: A website should not have a confusing navigation system. Users should be able to find what they're looking for quickly and easily. Inconsistent Design: Inconsistencies in fonts, colors, or overall design can make your website look unprofessional. The design should be consistent throughout all pages. Slow Loading Times: Large images, animations, or other elements that significantly slow down page loading times should be avoided. Slow websites can lead to a poor user experience and high bounce rates. Poor Mobile Experience: Given the prevalence of mobile browsing, a design that doesn't perform well on mobile devices is a definite no. Autoplay Media: Videos or audio clips that start playing automatically can be annoying to users and should generally be avoided. Inaccessible Content: Ensure that all content is accessible to users of all abilities. Avoid design elements that violate accessibility standards. Hidden Contact Information: Contact information should be easy to find. Do not hide it in obscure parts of the website. Pop-ups: While sometimes necessary for marketing strategies, excessive use of pop-ups can annoy users and distract from the main content. Outdated Plugins: Avoid using outdated plugins or technology that some users may not be able to load or that could pose security risks. Lack of Privacy Policy: A website must have a clear and accessible privacy policy. Not having one can damage trust and may also violate laws or regulations.

```html
<!DOCTYPE html>
<html lang="en">
<head>
<meta charset="utf-8">
<title>Stridewell Equine Insurance</title>
<link rel="stylesheet" href="https://fonts.googleapis.com/css2?family=Oswald:wght@400;500&family=Poppins:wght@400;500;600&display=swap">
<style>
:root{
  --ink:#151515;
  --text:#444;
  --muted:#777;
  --line:#d8d8d8;
  --band:#eeeeee;
  --field:#f3f3f3;
  --dark:#141414;
  --slate:#3b3b3b;
  --star:#f2a21b;
  --accent-block:#2a2a2a;
  --white:#fff;
}
*{box-sizing:border-box;margin:0;padding:0}
html,body{width:1200px;height:4454px;overflow:hidden}
body{position:relative;background:var(--white);font-family:"Poppins",sans-serif;color:var(--text);font-size:13px}
.abs{position:absolute}
.display{font-family:"Oswald",sans-serif;font-weight:400;color:var(--ink);text-transform:uppercase;letter-spacing:-.5px}
.btn{position:absolute;display:flex;align-items:center;justify-content:center;border:2px solid var(--ink);font-family:"Oswald",sans-serif;font-weight:500;font-size:15px;color:var(--ink);text-transform:uppercase;background:transparent}
.brand{display:flex;align-items:center;gap:10px;font-family:"Oswald",sans-serif;font-weight:500;font-size:32px;letter-spacing:3px;color:var(--ink);text-transform:uppercase}
.brand .mark{width:34px;height:34px;border-radius:50%;border:2px solid currentColor}

/* header */
.site-header{position:absolute;left:0;top:0;width:1200px;height:80px;background:var(--white);z-index:3}
.site-header .brand{position:absolute;left:88px;top:20px}
.nav{position:absolute;left:474px;top:0;height:80px;display:flex;align-items:center;gap:27px;font-family:"Oswald",sans-serif;font-size:12.5px;color:var(--ink);text-transform:uppercase}
.nav .claim{border:2px solid var(--ink);padding:9px 22px;font-weight:500;margin-left:2px}

/* hero */
.hero{position:absolute;left:0;top:80px;width:1200px;height:800px;background:linear-gradient(180deg,#fbf7f4 0%,#f6eee6 45%,#ead4b5 72%,#d7b284 100%)}
.hero-photo{position:absolute;left:690px;top:120px;width:510px;height:600px;background:radial-gradient(ellipse at 55% 45%,#e9e5e0 0%,#d9d2ca 40%,rgba(230,220,208,0) 72%)}
.hero h1{position:absolute;left:88px;top:248px;font-size:52px;line-height:57px;width:600px;letter-spacing:-1.2px}
.hero .btn{left:88px;top:434px;width:143px;height:52px}
.wave{position:absolute;left:0;width:1200px}

/* about */
.about-photo{position:absolute;left:148px;top:773px;width:407px;height:545px;background:linear-gradient(135deg,#8aa7c6 0%,#7a5a3c 45%,#b5a07e 75%,#6f8a4a 100%)}
.about-accent{position:absolute;left:122px;top:1218px;width:124px;height:124px;background:linear-gradient(90deg,var(--accent-block) 0 16px,transparent 16px),linear-gradient(0deg,var(--accent-block) 0 16px,transparent 16px);opacity:.85}
.about-copy{position:absolute;left:612px;top:958px;width:440px}
.about-copy h2{font-size:52px;margin-bottom:10px}
.about-copy p{font-size:12.6px;line-height:23px;color:var(--text)}
.about-copy .more{display:block;margin:26px 0 0 36px;font-family:"Oswald",sans-serif;font-weight:500;font-size:15px;color:var(--ink)}

/* services */
.section-title{position:absolute;left:0;width:1200px;text-align:center;font-size:52px}
.services-lede{position:absolute;left:300px;top:1496px;width:600px;text-align:center;font-size:13px;line-height:23px}
.grey-band{position:absolute;left:0;top:1766px;width:1200px;height:300px;background:var(--band)}
.cards{position:absolute;left:88px;top:1570px;width:1024px;display:flex;gap:8px}
.card{width:250px;height:375px;background:var(--white);box-shadow:0 4px 18px rgba(0,0,0,.08)}
.card .ph{height:196px}
.card h3{font-family:"Oswald",sans-serif;font-weight:400;font-size:17px;color:var(--ink);text-transform:uppercase;margin:30px 26px 4px}
.card p{font-size:12px;line-height:18px;margin:0 26px;color:var(--text)}

/* quote */
.quote-photo{position:absolute;left:180px;top:2104px;width:420px;height:402px;background:linear-gradient(180deg,#f6f6f6 0%,#eeeeee 48%,#cfd6dc 62%,#8a5a36 82%,#6a7d52 100%)}
.quote-title{position:absolute;left:263px;top:2180px;font-size:44px;line-height:46px;letter-spacing:-1.2px}
.dark-band{position:absolute;left:0;top:2506px;width:1200px;height:360px;background:linear-gradient(90deg,#3d3d3d 0%,#4a4a4a 50%,#2e2e2e 100%)}
.quote-form{position:absolute;left:600px;top:2104px;width:422px;height:506px;background:var(--white);box-shadow:0 6px 24px rgba(0,0,0,.12);padding:48px 43px 0}
.row{display:flex;gap:8px;margin-bottom:9px}
.field{flex:1;height:42px;background:var(--field);display:flex;align-items:center;justify-content:space-between;padding:0 18px;font-size:12px;color:#555}
.submit{height:42px;background:var(--dark);color:var(--white);display:flex;align-items:center;justify-content:center;font-weight:600;font-size:12.5px;text-transform:uppercase}
.claim-title{position:absolute;left:188px;top:2660px;font-size:48px;line-height:56px;color:var(--white);letter-spacing:-1px}
.dark-band-btn{left:847px;top:2702px;width:174px;height:50px;border-color:var(--white);color:var(--white)}

/* blog */
.posts{position:absolute;left:88px;top:3047px;width:1024px;display:flex;gap:11px}
.post{width:334px;height:403px;background:var(--white);box-shadow:0 4px 18px rgba(0,0,0,.08)}
.post .ph{height:228px}
.post h3{font-family:"Oswald",sans-serif;font-weight:400;font-size:18px;color:var(--ink);text-transform:uppercase;margin:22px 33px 6px}
.meta{display:flex;gap:18px;margin:0 33px 10px;font-size:11.5px;color:#999}
.post p{font-size:12px;line-height:18px;margin:0 33px;color:var(--text)}
.post .more{display:block;margin:10px 33px 0;font-family:"Oswald",sans-serif;font-weight:500;font-size:12px;color:var(--ink)}

/* review */
.review-text{position:absolute;left:270px;top:3708px;width:660px;text-align:center;font-size:13px;line-height:23px}
.arrow{position:absolute;width:40px;height:40px;border-radius:50%;background:#f2f2f2;display:flex;align-items:center;justify-content:center}
.stars{position:absolute;left:0;top:3780px;width:1200px;text-align:center;color:var(--star);font-size:14px;letter-spacing:4px}
.reviewer{position:absolute;left:0;top:3802px;width:1200px;text-align:center;font-weight:600;font-size:15px;color:var(--ink)}

/* footer */
.footer{position:absolute;left:0;top:3980px;width:1200px;height:474px;background:var(--dark);color:#ddd}
.footer .brand{position:absolute;left:88px;top:198px;color:var(--white);font-size:40px}
.fcol{position:absolute;top:128px}
.fcol h4{font-family:"Oswald",sans-serif;font-weight:400;font-size:23px;color:var(--white);text-transform:uppercase;margin-bottom:6px}
.fcol li{list-style:none;font-size:13px;line-height:22px;color:#ddd}
.subscribe{margin-top:12px;width:254px;height:48px;background:#2b2b2b;display:flex;align-items:center;justify-content:space-between;padding:0 18px;font-size:13px;color:#ddd}
.contact li{display:flex;align-items:center;gap:8px}
.social{display:flex;gap:10px;margin-top:8px}
.social span{width:10px;height:10px;border-radius:50%;background:var(--white)}
.footer hr{position:absolute;left:88px;top:415px;width:1024px;border:0;border-top:1px solid #333}
.copyright{position:absolute;left:0;top:432px;width:1200px;text-align:center;font-size:12px;color:#ddd}
.chat{position:absolute;left:1112px;top:4368px;width:66px;height:66px;border-radius:50%;background:var(--white);display:flex;align-items:center;justify-content:center}
</style>
</head>
<body>

<header class="site-header">
  <div class="brand"><span class="mark"></span>Stridewell</div>
  <nav class="nav">
    <svg width="14" height="13" viewBox="0 0 14 13" aria-label="Home"><path d="M7 0 0 6h2v7h4V9h2v4h4V6h2z" fill="#151515"/></svg>
    <span>About Us</span><span>Services/Products</span><span>Get a Quote</span><span>Blog</span><span>Contact Us</span>
    <span class="claim">File a Claim</span>
    <svg width="18" height="18" viewBox="0 0 18 18" aria-label="Account"><circle cx="9" cy="6" r="4" fill="none" stroke="#151515" stroke-width="1.4"/><path d="M2 17c1-4 4-6 7-6s6 2 7 6" fill="none" stroke="#151515" stroke-width="1.4"/></svg>
  </nav>
</header>

<section class="hero">
  <div class="hero-photo" role="img" aria-label="White horse leaping across a sandy arena"></div>
  <h1 class="display">Insure your horse's health, safety, and well-being with equine insurance.</h1>
  <span class="btn">Get a Quote</span>
</section>
<svg class="wave" style="top:760px" height="140" viewBox="0 0 1200 140" preserveAspectRatio="none">
  <path d="M0 50 C150 10 260 70 420 60 C620 45 700 20 900 30 C1050 40 1140 100 1200 120 L1200 140 L0 140Z" fill="#151515"/>
  <path d="M0 58 C150 20 260 80 420 70 C620 55 700 34 900 44 C1050 54 1140 112 1200 132 L1200 140 L0 140Z" fill="#fff"/>
</svg>

<section class="about">
  <div class="about-accent" role="img" aria-label="Decorative dotted corner accent"></div>
  <div class="about-photo" role="img" aria-label="Smiling horse owner beside two horses"></div>
  <div class="about-copy">
    <h2 class="display">About Stridewell</h2>
    <p>Lorem Ipsum is simply dummy text of the printing and typesetting industry. Lorem Ipsum has been the industry's standard dummy text ever since the 1500s, when an unknown printer took a galley of type and scrambled it to make a type specimen book. It has survived not only five centuries, but also the leap into electronic typesetting, remaining essentially unchanged. It was popularised in the 1960s with the release of Letraset sheets</p>
    <span class="more">READ MORE</span>
  </div>
</section>

<section class="services">
  <h2 class="display section-title" style="top:1428px">Services Stridewell</h2>
  <p class="services-lede">We offer customized equine insurance policies to protect your horses and your financial interests. Trust us for comprehensive coverage tailored to your needs.</p>
  <div class="grey-band"></div>
  <div class="cards">
    <article class="card"><div class="ph" role="img" aria-label="Mare and foal standing together" style="background:linear-gradient(160deg,#a9c3d8,#6b4528 60%,#3d2616)"></div><h3>Mortality Insurance</h3><p>Protect your horses from unexpected loss or death with our comprehensive coverage for accidents, illnesses, and natural causes.</p></article>
    <article class="card"><div class="ph" role="img" aria-label="Vet examining a grey horse outdoors" style="background:linear-gradient(160deg,#7aa05a,#2f8f73 45%,#cfc7bd)"></div><h3>Medical Coverage</h3><p>Ensure your horses receive the best veterinary care with our insurance plans covering diagnostics, treatments, surgeries, medications, and rehabilitation.</p></article>
    <article class="card"><div class="ph" role="img" aria-label="Paint horse in a stable stall" style="background:linear-gradient(160deg,#555,#8a5a3c 50%,#e4e0dc)"></div><h3>Liability Coverage</h3><p>Safeguard yourself against property damage or bodily injury claims caused by your horses with our liability insurance.</p></article>
    <article class="card"><div class="ph" role="img" aria-label="Vet and owner checking a horse in a paddock" style="background:linear-gradient(180deg,#8fb7e3,#b7d2ea 45%,#5d8a3a 70%,#3b5d25)"></div><h3>Customized Solutions</h3><p>Get personalized insurance plans tailored to your specific needs, providing the right level of coverage for your horses and peace of mind.</p></article>
  </div>
  <span class="btn" style="left:513px;top:1987px;width:174px;height:50px">Online Purhase</span>
</section>

<section class="quote">
  <div class="dark-band" role="img" aria-label="Faded insurance claim paperwork"></div>
  <div class="quote-photo" role="img" aria-label="Rider jumping a chestnut horse"></div>
  <h2 class="display quote-title">Horse<br>Insurance Quote</h2>
  <form class="quote-form">
    <div class="row"><div class="field">Title<svg width="9" height="6"><path d="M1 1l3.5 3.5L8 1" stroke="#333" fill="none" stroke-width="1.3"/></svg></div><div class="field">First Name</div></div>
    <div class="row"><div class="field">Last Name</div><div class="field">E-mail</div></div>
    <div class="row"><div class="field">DOB<svg width="12" height="12"><rect x="1" y="2" width="10" height="9" fill="none" stroke="#777"/><path d="M1 5h10" stroke="#777"/></svg></div><div class="field">Mobile</div></div>
    <div class="row"><div class="field">Phone</div><div class="field">Street Address</div></div>
    <div class="row"><div class="field">Post code / Suburb</div><div class="field">Country<svg width="9" height="6"><path d="M1 1l3.5 3.5L8 1" stroke="#333" fill="none" stroke-width="1.3"/></svg></div></div>
    <div class="row"><div class="field">Where did you hear about us<svg width="9" height="6"><path d="M1 1l3.5 3.5L8 1" stroke="#333" fill="none" stroke-width="1.3"/></svg></div></div>
    <div class="row"><div class="field">Do you have a promotion code?<svg width="9" height="6"><path d="M1 1l3.5 3.5L8 1" stroke="#333" fill="none" stroke-width="1.3"/></svg></div></div>
    <div class="submit">Submit Now</div>
  </form>
  <h2 class="display claim-title">What type of claim are<br>you reporting?</h2>
  <span class="btn dark-band-btn">Insurance Claim</span>
</section>

<section class="blog">
  <h2 class="display section-title" style="top:2960px">Latest Blog</h2>
  <div class="posts">
    <article class="post"><div class="ph" role="img" aria-label="Rider leaning on a fence beside her horse" style="background:linear-gradient(160deg,#b9c9a8,#7b4a2c 55%,#9a9a9a)"></div><h3>Producers Delight</h3><div class="meta"><span>▭ Gear</span><span>1 Comment</span></div><p>Id per diceret propriae mediocrem, pro ea utamur dolores democritum. Ei eam convenire...</p><span class="more">READ MORE</span></article>
    <article class="post"><div class="ph" role="img" aria-label="Two handlers with a horse in a stable" style="background:linear-gradient(160deg,#d7d2c4,#7d5a3a 45%,#3a5a3a)"></div><h3>Producers Delight</h3><div class="meta"><span>▭ Gear</span><span>1 Comment</span></div><p>Id per diceret propriae mediocrem, pro ea utamur dolores democritum. Ei eam convenire...</p><span class="more">READ MORE</span></article>
    <article class="post"><div class="ph" role="img" aria-label="Vet treating a horse in a clinic" style="background:linear-gradient(160deg,#6b4a30,#8a5a3a 40%,#9cc3e6 70%,#e8eef2)"></div><h3>Producers Delight</h3><div class="meta"><span>▭ Gear</span><span>1 Comment</span></div><p>Id per diceret propriae mediocrem, pro ea utamur dolores democritum. Ei eam convenire...</p><span class="more">READ MORE</span></article>
  </div>
</section>

<section class="review">
  <h2 class="display section-title" style="top:3545px">Customer Review</h2>
  <svg class="abs" style="left:562px;top:3640px" width="76" height="64" viewBox="0 0 76 64"><path d="M0 36C0 14 12 2 30 0v12C20 14 16 22 16 28h14v36H0zM42 36C42 14 54 2 72 0v12C62 14 58 22 58 28h14v36H42z" fill="#151515"/></svg>
  <span class="arrow" style="left:190px;top:3706px"><svg width="12" height="10"><path d="M11 5H1M5 1 1 5l4 4" stroke="#444" fill="none" stroke-width="1.2"/></svg></span>
  <p class="review-text">Lorem Ipsum is simply dummy text of the printing and typesetting industry. Lorem Ipsum has been the industry's standard dummy text ever since the 1500s, when an unknown printer took a galley of type and scrambled it to make a type specimen book.</p>
  <span class="arrow" style="left:970px;top:3706px"><svg width="12" height="10"><path d="M1 5h10M7 1l4 4-4 4" stroke="#444" fill="none" stroke-width="1.2"/></svg></span>
  <div class="stars">★★★★★</div>
  <div class="reviewer">John Doe</div>
</section>

<svg class="wave" style="top:3860px" height="130" viewBox="0 0 1200 130" preserveAspectRatio="none">
  <path d="M0 90 C120 110 260 60 420 62 C600 66 720 110 900 82 C1040 60 1130 20 1200 0 L1200 130 L0 130Z" fill="#151515"/>
</svg>
<footer class="footer">
  <div class="brand"><span class="mark"></span>Stridewell</div>
  <div class="fcol" style="left:381px"><h4>Useful Links</h4><ul><li>Home</li><li>About Us</li><li>Services</li><li>Get a Quote</li><li>Contact Us</li><li>File a claim</li><li>Blog</li></ul></div>
  <div class="fcol" style="left:592px"><h4>Newsletter</h4><ul><li>Subscribe to Our newsletter</li></ul>
    <div class="subscribe">Email Address<svg width="13" height="13"><path d="M1 6 12 1 7 12 6 7z" fill="#ddd"/></svg></div></div>
  <div class="fcol contact" style="left:904px"><h4>Contact Us</h4><ul>
    <li><svg width="9" height="12"><path d="M4.5 0A4.5 4.5 0 0 0 0 4.5C0 8 4.5 12 4.5 12S9 8 9 4.5A4.5 4.5 0 0 0 4.5 0z" fill="#fff"/></svg>Some goes address here</li>
    <li><svg width="11" height="9"><rect width="11" height="9" fill="#fff"/><path d="M0 0l5.5 5L11 0" stroke="#151515" fill="none"/></svg>info@example.com</li>
    <li><svg width="11" height="11"><path d="M2 0l3 3-1.5 1.5a7 7 0 0 0 3 3L8 6l3 3-2 2C4 11 0 7 0 2z" fill="#fff"/></svg>+123 458 55666</li>
    <li><svg width="11" height="11"><circle cx="5.5" cy="5.5" r="5" fill="none" stroke="#fff"/><path d="M0.5 5.5h10M5.5 0.5v10" stroke="#fff"/></svg>www.example.com</li></ul>
    <div class="social"><span></span><span></span><span></span><span></span></div></div>
  <hr>
  <p class="copyright">©Copyright Stridewell 2023 | All Rights Reserved</p>
</footer>
<div class="chat" aria-label="Chat"><svg width="34" height="32" viewBox="0 0 34 32"><path d="M17 2C8 2 2 8 2 15c0 4 2 7 5 9l-2 6 7-4c2 1 3 1 5 1 9 0 15-6 15-12S26 2 17 2z" fill="#151515"/></svg></div>

</body>
</html>
```